Software Company Business Card

We are looking for a new design of our business card. The design will also be used in the rest of our branding and marketing materials as we want to keep it all uniform. We sell POS software to fine/luxury jewelers and also offer other business services as well to help the jeweler manage their business and need something more updated, technical and fresh, preferably more on the masculine side. We do not want any designs with gems in them but if possible would like to incorporate the circle and arrow in the logo into the design, but not a requirement if you can't make it work. I would like to see a variety of the mix. The colors need to remain our blue and orange and the logo can not change. The squiggly lines have been used as our corporate identity for over 20 years and its time to update. Our company name is TELK (Summit Counter Operations Platform).

Target Market(s)

High End Jewelers

Industry/Entity Type

Software

Contact Information for Business Card

Requirements
Must have
• Our logo and the colors must remain the same. Blue is #d95d39 and Orange is #0f5682.
Nice to have
• The circle and arrow incorporated but not a requirement.
Should not have
• Anything jewelry or gem related.

```html
<!DOCTYPE html>
<html lang="en">
<head>
<meta charset="utf-8">
<title>TELK Business Card – Front and Back</title>
<link href="https://fonts.googleapis.com/css2?family=IBM+Plex+Sans:wght@300;400;700&display=swap" rel="stylesheet">
<style>
  :root {
    --brand-orange: #d95d39;
    --brand-blue: #0b5583;
    --card-white: #ffffff;
    --badge-gold: #c9a55a;
    --badge-green: #9fbcb0;
  }
  * { margin: 0; padding: 0; box-sizing: border-box; }
  html, body { width: 1200px; height: 1200px; overflow: hidden; }
  body {
    background: var(--brand-orange);
    font-family: "IBM Plex Sans", Arial, sans-serif;
    position: relative;
  }
  .card {
    position: absolute;
    left: 262px;
    width: 676px;
    height: 396px;
    background: var(--card-white);
    overflow: hidden;
    box-shadow: 6px 8px 14px rgba(90, 30, 10, 0.35);
  }
  .card--front { top: 138px; }
  .card--back { top: 665px; }
  .card__band {
    position: absolute; left: 0; top: 0;
    width: 23px; height: 100%;
    background: var(--brand-blue);
  }
  .card__disc {
    position: absolute;
    left: 480px; top: 105px;
    width: 310px; height: 310px;
    border-radius: 50%;
    background: var(--brand-orange);
  }
  .wordmark {
    position: absolute;
    display: flex; align-items: center;
    color: var(--brand-blue);
    font-weight: 700;
    line-height: 1;
  }
  .wordmark__dot { border-radius: 50%; background: var(--brand-orange); flex: none; }
  .wordmark--small { left: 394px; top: 31px; font-size: 44px; gap: 10px; }
  .wordmark--small .wordmark__dot { width: 50px; height: 50px; }
  .wordmark--large { left: 57px; top: 52px; font-size: 104px; gap: 22px; }
  .wordmark--large .wordmark__dot { width: 90px; height: 90px; }

  .person { position: absolute; left: 47px; top: 110px; color: var(--brand-blue); }
  .person__name { font-size: 32px; font-weight: 700; line-height: 1.1; }
  .person__title { font-size: 15px; font-weight: 300; margin-top: 1px; }
  .card__rule {
    position: absolute; left: 23px; top: 186px;
    width: 55px; height: 4px;
    background: var(--brand-orange);
  }
  .contact {
    position: absolute; top: 207px;
    color: var(--brand-blue);
    font-size: 15.5px; font-weight: 300; line-height: 19px;
  }
  .contact--details { left: 47px; }
  .contact--address { left: 302px; }
  .contact__row { display: flex; }
  .contact__label { width: 47px; }

  .partner {
    position: absolute;
    height: 44px;
    border-radius: 4px;
  }
  .partner--show { background: var(--badge-gold); opacity: 0.55; width: 126px; }
  .partner--society { background: var(--badge-green); opacity: 0.5; width: 179px; }
  .card--front .partner { top: 322px; }
  .card--front .partner--show { left: 47px; }
  .card--front .partner--society { left: 209px; }
  .card--back .partner { top: 322px; }
  .card--back .partner--show { left: 55px; }
  .card--back .partner--society { left: 217px; }
</style>
</head>
<body>
  <section class="card card--front" aria-label="Business card front">
    <div class="card__band"></div>
    <div class="card__disc"></div>
    <div class="wordmark wordmark--small">
      <span class="wordmark__text">TELK</span>
      <span class="wordmark__dot"></span>
    </div>
    <div class="person">
      <h1 class="person__name">Graham Whitcombe</h1>
      <p class="person__title">Director of Global Operations</p>
    </div>
    <div class="card__rule"></div>
    <div class="contact contact--details">
      <div class="contact__row"><span class="contact__label">Phone</span><span>: +1 555 014-2281</span></div>
      <div class="contact__row"><span class="contact__label">Fax</span><span>: +1 555 014-2290</span></div>
      <div class="contact__row"><span class="contact__label">Email</span><span>: graham@telkpos.com</span></div>
      <div class="contact__row"><span class="contact__label">Web</span><span>: www.telkpos.com</span></div>
    </div>
    <div class="contact contact--address">
      <div>1480 Meridian Parkway</div>
      <div>Suite 210</div>
      <div>Lakeview, NV 89000</div>
      <div>USA</div>
    </div>
    <div class="partner partner--show" role="img" aria-label="Partner trade show badge"></div>
    <div class="partner partner--society" role="img" aria-label="Partner society membership badge"></div>
  </section>

  <section class="card card--back" aria-label="Business card back">
    <div class="card__band"></div>
    <div class="card__disc"></div>
    <div class="wordmark wordmark--large">
      <span class="wordmark__text">TELK</span>
      <span class="wordmark__dot"></span>
    </div>
    <div class="partner partner--show" role="img" aria-label="Partner trade show badge"></div>
    <div class="partner partner--society" role="img" aria-label="Partner society membership badge"></div>
  </section>
</body>
</html>
```